TeeVista Stationery and Style Guide, You set the tone! (logo Provided)

TeeVista is a new and exciting business that will be focusing on providing quality golf information for all Australian golfers.

We already have a great logo and now we are looking to style our documents.

We would like to see the following:

- Front cover page Design including(logo, branding statement and Document title) Branding statement is Every Green - Every Swing
- Sales Document design, this is our main document and we would like you to spend most time on this document. I have attached a sample PDF with the basic layout. but you will need to add some flair to the document and make it look great.
- A Dot point design explaining points in an image (I have attached a sample to show what I mean) Please include this image in the Sales Document
- A footnote for all documents(containing, small logo, branding statement and website address)
- An email signature (containing: logo, Dane Pellow, dane@teevista.com.au, 0471 582 913, www.teevista.com.au)

The font used in the logo is borisblackboxx.
At this stage we don't need business cards or envelopes please.

A little background:
The service will be providing:

• A Website that allows all Australian golfers to find golf courses close to them on a simple to use Google map
• Browse golf courses on a map or by search.
• View full information about a golf course including images, facilities, prices and full contact details.
• Mobile version of the website for Iphone, Android and other mobile platforms.
• We will use the users GPS location to show them where they are and what golf courses are near them.
• All golf courses will be able to show specials and other deals for all visitors.

Thank you for looking at our project and we look forward to your designs.

Target Market(s)

All Australian Golfers

Industry/Entity Type

Golf Course

Requirements
Must have
• A great Sales Document Design as that is the main stationery document we will be using.
Please use the sample Sales Document for sample content and basic elements needed.
Should not have
• We don't need business cards and envelope design.

```html
<!DOCTYPE html>
<html lang="en">
<head>
<meta charset="utf-8">
<title>TeeVista Stationery</title>
<link rel="stylesheet" href="https://fonts.googleapis.com/css2?family=Arimo:wght@400;700&display=swap">
<style>
  :root {
    --backdrop: #e9e6e1;
    --paper: #ffffff;
    --green-deep: #5ea226;
    --green-mid: #8dc63f;
    --green-light: #c9e03a;
    --text-green: #7ab83b;
    --heading-orange: #f39a1e;
    --caption: #4a4540;
    --ghost: #e2e4e3;
    --ghost-dark: #cfd2d1;
    --grey-text: #6d6d6d;
    --callout-red: #e0473a;
  }
  * { margin: 0; padding: 0; box-sizing: border-box; }
  html, body { width: 1200px; height: 561px; overflow: hidden; }
  body {
    position: relative;
    background: var(--backdrop);
    font-family: "Arimo", Arial, sans-serif;
  }
  .page {
    position: absolute; top: 20px; width: 339px; height: 438px;
    background: var(--paper);
    box-shadow: 0 2px 6px rgba(0,0,0,.18);
    overflow: hidden;
  }
  .page--cover { left: 42px; }
  .page--intro { left: 426px; }
  .page--benefits { left: 809px; }
  .page-header { position: absolute; top: 0; left: 0; width: 339px; height: 90px; }
  .brand {
    position: absolute; display: flex; align-items: center; gap: 4px;
    font-weight: 700; color: #ffffff;
  }
  .page .brand { top: 44px; left: 16px; font-size: 17px; }
  .brand-dot { width: 10px; height: 10px; border-radius: 50%; background: #ffffff; }
  .tagline {
    position: absolute; top: 36px; left: 145px;
    color: #ffffff; font-size: 7.5px; font-weight: 700;
    transform: rotate(-6deg); transform-origin: left;
  }
  .golfer-art {
    position: absolute; right: 6px; bottom: 14px; width: 82px; height: 132px;
    background: linear-gradient(180deg, var(--ghost) 0%, var(--ghost-dark) 100%);
    border-radius: 40px 30px 6px 6px; opacity: .8;
  }
  .page-footer {
    position: absolute; left: 20px; right: 20px; bottom: 7px;
    display: flex; justify-content: space-between;
    font-size: 5.5px; font-weight: 700; color: var(--text-green);
  }
  .page-content { position: absolute; top: 82px; left: 36px; width: 260px; }
  .section-title {
    color: var(--heading-orange); font-size: 8px; font-weight: 700; margin-bottom: 8px;
  }
  .body-copy { color: var(--text-green); font-size: 5.6px; line-height: 7.3px; margin-bottom: 7px; }
  .bullet-list { list-style: none; color: var(--text-green); font-size: 5.6px; line-height: 7.3px; margin-bottom: 7px; }
  .bullet-list li::before { content: "•"; margin-right: 4px; }
  .phone-feature { position: absolute; left: 30px; top: 270px; width: 280px; height: 168px; }
  .phone-device {
    position: absolute; left: 81px; top: 12px; width: 114px; height: 156px;
    border-radius: 14px 14px 0 0;
    background: linear-gradient(160deg, #3a3a3a 0%, #9fb6c9 40%, #c5d9e6 70%, #2a2a2a 100%);
  }
  .callout-note {
    position: absolute; font-size: 3.6px; line-height: 4.4px; font-weight: 700;
    color: var(--grey-text); text-transform: uppercase; width: 44px;
  }
  .caption { position: absolute; font-size: 9px; color: var(--caption); }
  .signature {
    position: absolute; background: var(--paper);
    box-shadow: 0 2px 5px rgba(0,0,0,.18); overflow: hidden;
  }
  .signature--side { left: 605px; top: 475px; width: 163px; height: 58px; }
  .signature--band { left: 928px; top: 478px; width: 157px; height: 55px; }
  .signature .brand { font-size: 10px; }
  .signature .brand-dot { width: 6px; height: 6px; }
  .sig-name { font-size: 5.5px; font-weight: 700; color: var(--grey-text); }
  .sig-contacts { font-size: 4.4px; line-height: 6px; color: var(--grey-text); }
</style>
</head>
<body>

<!-- Cover page -->
<section class="page page--cover">
  <svg class="page-header" viewBox="0 0 339 90" aria-hidden="true">
    <defs>
      <linearGradient id="bandA" x1="0" x2="1"><stop offset="0" stop-color="#5ea226"/><stop offset="1" stop-color="#c9e03a"/></linearGradient>
    </defs>
    <path d="M0 0H339V26C250 36 170 40 95 58C60 66 30 72 0 76Z" fill="url(#bandA)"/>
    <path d="M0 76C30 72 60 66 95 58C170 40 250 36 339 26V32C250 42 170 46 95 63C60 71 30 78 0 82Z" fill="#c9e03a" opacity=".55"/>
  </svg>
  <div class="brand"><span class="brand-dot"></span>TeeVista</div>
  <div class="tagline">Every Green - Every Swing</div>
  <div class="golfer-art" role="img" aria-label="Faint silhouette of a golfer putting"></div>
  <footer class="page-footer"><span>Every Green - Every Swing</span><span>www.teevista.com.au</span></footer>
</section>

<!-- Introduction page -->
<section class="page page--intro">
  <svg class="page-header" viewBox="0 0 339 90" aria-hidden="true">
    <path d="M0 0H339V26C250 36 170 40 95 58C60 66 30 72 0 76Z" fill="url(#bandA)"/>
    <path d="M0 76C30 72 60 66 95 58C170 40 250 36 339 26V32C250 42 170 46 95 63C60 71 30 78 0 82Z" fill="#c9e03a" opacity=".55"/>
  </svg>
  <div class="brand"><span class="brand-dot"></span>TeeVista</div>
  <div class="tagline">Every Green - Every Swing</div>
  <div class="golfer-art" role="img" aria-label="Faint silhouette of a golfer putting"></div>
  <div class="page-content">
    <h2 class="section-title">Introduction</h2>
    <p class="body-copy">Lorem ipsum dolor sit amet, consectetur adipiscing elit. Mauris auctor elit nec neque dictum ultricies. Suspendisse potenti. Etiam eget orci lorem, a commodo enim.</p>
    <p class="body-copy">Donec massa turpis, pulvinar sit amet luctus at, tempor at lorem. Mauris nec massa augue. Phasellus dictum, metus vel posuere ullamcorper, risus erat vehicula magna, id facilisis orci tellus ac magna. Nam a augue lacus, id tempor lorem.</p>
    <p class="body-copy">Mauris odio nunc, dignissim et fermentum eget, venenatis quis turpis. Phasellus faucibus, ligula id pulvinar adipiscing, tortor erat pretium felis, posuere pretium neque nulla pretium lectus. Nulla facilisi. Donec at suscipit quam. Nulla non tortor orci. Fusce purus sem, rutrum et egestas ac, consequat a mi. Curabitur tincidunt massa eget mauris sagittis ornare imperdiet tortor vulputate.</p>
    <p class="body-copy">Aenean blandit eros et neque rhoncus sed tristique ante euismod. Curabitur quis nisi quis mi dapibus faucibus sit amet id enim.</p>
    <p class="body-copy">Ut sed dictum dui. Aenean convallis sagittis ipsum, sed tempor dui ultricies sit amet. Praesent sed erat odio. Duis odio elit, commodo vel luctus non, laoreet at eros. Nullam a mauris metus.</p>
  </div>
  <div class="phone-feature">
    <div class="phone-device" role="img" aria-label="Smartphone showing an interactive map of nearby golf courses with location pins"></div>
    <svg width="280" height="168" style="position:absolute;left:0;top:0" aria-hidden="true">
      <g stroke="var(--callout-red)" stroke-width=".8" fill="var(--callout-red)">
        <line x1="56" y1="50" x2="118" y2="90"/><circle cx="118" cy="90" r="2"/>
        <line x1="48" y1="150" x2="140" y2="150"/><circle cx="140" cy="150" r="2"/><circle cx="48" cy="150" r="2"/>
        <line x1="212" y1="50" x2="170" y2="110"/><circle cx="170" cy="110" r="2"/>
      </g>
    </svg>
    <div class="callout-note" style="left:10px;top:34px">Info message about dot point</div>
    <div class="callout-note" style="left:2px;top:126px">Interactive map lets users find more courses</div>
    <div class="callout-note" style="left:206px;top:34px">List a special and get a featured listing</div>
  </div>
  <footer class="page-footer"><span>Every Green - Every Swing</span><span>www.teevista.com.au</span></footer>
</section>

<!-- Benefits page -->
<section class="page page--benefits">
  <svg class="page-header" viewBox="0 0 339 90" aria-hidden="true">
    <path d="M0 0H339V26C250 36 170 40 95 58C60 66 30 72 0 76Z" fill="url(#bandA)"/>
    <path d="M0 76C30 72 60 66 95 58C170 40 250 36 339 26V32C250 42 170 46 95 63C60 71 30 78 0 82Z" fill="#c9e03a" opacity=".55"/>
  </svg>
  <div class="brand"><span class="brand-dot"></span>TeeVista</div>
  <div class="tagline">Every Green - Every Swing</div>
  <div class="golfer-art" role="img" aria-label="Faint silhouette of a golfer putting"></div>
  <div class="page-content">
    <h2 class="section-title">Benefits</h2>
    <p class="body-copy">Lorem ipsum dolor sit amet, consectetur adipiscing elit. Mauris auctor elit nec neque dictum ultricies. Suspendisse potenti. Etiam eget orci lorem, a commodo enim.</p>
    <ul class="bullet-list">
      <li>Donec massa turpis, pulvinar sit amet luctus at, tempor at lorem.</li>
      <li>Mauris nec massa augue. Phasellus dictum, metus vel posuere ullamcorper, risus erat vehicula magna, id facilisis orci tellus ac magna.</li>
      <li>Nam a augue lacus, id tempor lorem. Mauris odio nunc, dignissim</li>
      <li>et fermentum eget, venenatis quis turpis. Phasellus faucibus,</li>
      <li>ligula id pulvinar adipiscing, tortor erat pretium felis, posuere</li>
      <li>pretium neque nulla pretium lectus.</li>
      <li>Nulla facilisi. Donec at suscipit quam. Nulla non tortor orci.</li>
      <li>Fusce purus sem, rutrum et egestas ac, consequat a mi.</li>
      <li>Curabitur tincidunt massa eget mauris sagittis</li>
      <li>ornare imperdiet tortor vulputate.</li>
    </ul>
    <p class="body-copy">Aenean blandit eros et neque rhoncus sed tristique ante euismod. Curabitur quis nisi quis mi dapibus faucibus sit amet id enim.</p>
    <p class="body-copy">Ut sed dictum dui. Aenean convallis sagittis ipsum, sed tempor dui ultricies sit amet. Praesent sed erat odio. Duis odio elit, commodo vel luctus non, laoreet at eros. Nullam a mauris metus. Aenean blandit eros et neque rhoncus sed tristique ante euismod. Curabitur quis nisi quis mi dapibus faucibus sit amet id enim.</p>
    <p class="body-copy">Ut sed dictum dui. Aenean convallis sagittis ipsum, sed tempor dui ultricies sit amet. Praesent sed erat odio. Duis odio elit, commodo vel luctus non, laoreet at eros. Nullam a mauris metus.</p>
  </div>
  <footer class="page-footer"><span>Every Green - Every Swing</span><span>www.teevista.com.au</span></footer>
</section>

<p class="caption" style="left:42px;top:463px">Document Page 1</p>
<p class="caption" style="left:426px;top:463px">Document Page 2</p>
<p class="caption" style="left:809px;top:463px">Document Page 3</p>

<!-- Email signature 1 -->
<section class="signature signature--side">
  <svg width="163" height="58" style="position:absolute;left:0;top:0" aria-hidden="true">
    <defs>
      <linearGradient id="sideBand" x1="0" x2="1"><stop offset="0" stop-color="#5ea226"/><stop offset="1" stop-color="#c9e03a"/></linearGradient>
    </defs>
    <path d="M0 0H70C55 20 30 30 0 34Z" fill="url(#sideBand)"/>
    <line x1="96" y1="8" x2="96" y2="50" stroke="#dddddd" stroke-width=".6"/>
  </svg>
  <div class="brand" style="top:16px;left:22px;color:var(--green-deep)"><span class="brand-dot" style="background:var(--green-deep)"></span>TeeVista</div>
  <div style="position:absolute;top:36px;left:22px;font-size:4.5px;font-weight:700;color:var(--grey-text)">Every Green - Every Swing</div>
  <div style="position:absolute;top:12px;left:101px">
    <div class="sig-name">Dane Pellow</div>
    <div class="sig-contacts">dane@teevista.com.au<br>0471 582 913<br>www.teevista.com.au</div>
  </div>
</section>

<!-- Email signature 2 -->
<section class="signature signature--band">
  <svg width="157" height="55" style="position:absolute;left:0;top:0" aria-hidden="true">
    <path d="M0 0H157V10C110 14 70 20 40 30C25 35 12 38 0 40Z" fill="url(#sideBand)"/>
  </svg>
  <div class="brand" style="top:9px;left:6px"><span class="brand-dot"></span>TeeVista</div>
  <div style="position:absolute;top:8px;left:68px;font-size:4.5px;font-weight:700;color:#fff;transform:rotate(-5deg)">Every Green - Every Swing</div>
  <div class="sig-name" style="position:absolute;top:42px;left:14px">Dane Pellow</div>
  <div class="sig-contacts" style="position:absolute;top:30px;left:100px">dane@teevista.com.au<br>0471 582 913<br>www.teevista.com.au</div>
</section>

<p class="caption" style="left:642px;top:540px">Email Signature 1</p>
<p class="caption" style="left:957px;top:540px">Email Signature 2</p>

</body>
</html>
```